Tarvin Group Business Card

Building Management company based in Sydney, Australia. We provide onsite management for commercial and residential buildings.
I would like a sophisticated minimalist design that indicates that we provide a high-end service. I would like a silver or metal look background or something similar.
The business card should have:
Name
Title
email
Office Phone
Mobile
Address
Website
The services that we provide should be prominent:
Building Management - Concierge - Caretaking - Cleaning

```html
<!DOCTYPE html>
<html lang="en">
<head>
<meta charset="utf-8">
<title>Tarvin Group Business Card</title>
<link href="https://fonts.googleapis.com/css2?family=Lato:wght@400;700;900&display=swap" rel="stylesheet">
<style>
  :root {
    --stage: #2b2b2d;
    --card: #ffffff;
    --card-shade: #eef0f2;
    --brand-blue: #2566ad;
    --deep-blue: #1d5597;
    --ink: #1a1a1a;
    --teal: #2aa7a5;
    --band-text: #dfe9f5;
  }
  * { box-sizing: border-box; margin: 0; padding: 0; }
  html, body {
    width: 1200px; height: 873px; overflow: hidden;
    background: var(--stage);
    font-family: 'Lato', sans-serif;
  }
  .canvas { position: relative; width: 1200px; height: 873px; }

  .card {
    position: absolute;
    width: 560px; height: 320px;
    background: linear-gradient(135deg, var(--card) 55%, var(--card-shade));
    overflow: hidden;
  }
  .card--front { left: 60px; top: 70px; }
  .card--back { left: 580px; top: 480px; }

  .wordmark {
    display: flex; align-items: center; gap: 12px;
    color: var(--brand-blue);
    font-weight: 900;
    letter-spacing: 1px;
    white-space: nowrap;
  }
  .wordmark__square {
    width: 26px; height: 26px; background: var(--brand-blue); flex: none;
  }

  /* bottom band */
  .band {
    position: absolute; left: 0; right: 0; bottom: 14px;
    height: 40px;
    background: var(--brand-blue);
    color: var(--band-text);
    display: flex; align-items: center; justify-content: center;
  }
  .band::before, .band::after {
    content: ""; position: absolute; left: 0; right: 0; height: 3px;
    background: var(--brand-blue);
  }
  .band::before { top: -8px; }
  .band::after { bottom: -8px; }

  /* front */
  .card--front .wordmark {
    position: absolute; left: 0; right: 0; top: 110px;
    justify-content: center; font-size: 44px;
  }
  .card--front .band__text {
    font-size: 13px; letter-spacing: 5px; font-weight: 700;
  }

  /* back */
  .card--back .wordmark {
    position: absolute; left: 34px; top: 150px; font-size: 27px; gap: 10px;
  }
  .card--back .wordmark__square { width: 22px; height: 22px; }
  .divider {
    position: absolute; left: 318px; top: 40px;
    width: 2px; height: 170px;
    background: linear-gradient(var(--deep-blue), var(--teal));
  }
  .contact { position: absolute; left: 340px; top: 30px; width: 210px; }
  .contact__heading { display: inline-block; }
  .contact__name {
    color: var(--deep-blue); font-weight: 900; font-size: 18px; letter-spacing: .3px;
  }
  .contact__title {
    color: var(--deep-blue); font-size: 10px; font-weight: 700; text-align: right;
    margin-top: -2px;
  }
  .contact__company {
    color: var(--ink); font-weight: 900; font-size: 9px; margin-top: 8px;
  }
  .contact__address {
    color: var(--brand-blue); font-size: 9px; font-weight: 700; line-height: 1.3;
    text-transform: uppercase;
  }
  .contact__list { list-style: none; margin-top: 18px; }
  .contact__item {
    display: flex; align-items: center; gap: 10px;
    font-size: 10.5px; color: var(--ink); margin-bottom: 5px;
  }
  .contact__icon { width: 17px; height: 17px; flex: none; }
  .card--back .band__text {
    font-size: 13px; letter-spacing: 1px; font-weight: 700; text-transform: uppercase;
    white-space: nowrap;
  }
</style>
</head>
<body>
<div class="canvas">

  <section class="card card--front" aria-label="Card front">
    <div class="wordmark"><span class="wordmark__square"></span>TARVIN GROUP</div>
    <div class="band"><span class="band__text">WWW.TARVINGROUP.COM</span></div>
  </section>

  <section class="card card--back" aria-label="Card back">
    <div class="wordmark"><span class="wordmark__square"></span>TARVIN GROUP</div>
    <div class="divider"></div>
    <div class="contact">
      <div class="contact__heading">
        <p class="contact__name">DANA ELLERY</p>
        <p class="contact__title">CEO</p>
      </div>
      <p class="contact__company">TARVIN GROUP LTD.</p>
      <p class="contact__address">14 Carrow Lane, Harlow Park,<br>Sydney NSW 2000, Australia</p>
      <ul class="contact__list">
        <li class="contact__item">
          <svg class="contact__icon" viewBox="0 0 17 17"><rect width="17" height="17" fill="#2566ad"/><path d="M5 4c1 0 1.5 2 1.2 2.6L5.6 7.4c.6 1.4 1.6 2.4 3 3l.8-.6c.6-.3 2.6.2 2.6 1.2 0 1-1 1.8-2 1.8C7 12.8 4.2 10 4.2 6 4.2 5 4.5 4 5 4z" fill="#fff"/></svg>
          +61 2 9000 4418
        </li>
        <li class="contact__item">
          <svg class="contact__icon" viewBox="0 0 17 17"><rect width="17" height="17" fill="#2566ad"/><rect x="5.5" y="3" width="6" height="11" rx="1" fill="#fff"/><rect x="6.5" y="4.5" width="4" height="6" fill="#2566ad"/></svg>
          +61 4 1200 7735
        </li>
        <li class="contact__item">
          <svg class="contact__icon" viewBox="0 0 17 17"><rect width="17" height="17" fill="#2566ad"/><rect x="3" y="5" width="11" height="7.5" fill="#fff"/><path d="M3 5l5.5 4.2L14 5" fill="none" stroke="#2566ad" stroke-width="1"/></svg>
          info@tarvingroup.com
        </li>
      </ul>
    </div>
    <div class="band"><span class="band__text">Building Management - Concierge - Caretaking - Cleaning</span></div>
  </section>

</div>
</body>
</html>
```